Velmora Biz Card 2019

New business card for Velmora Property Inspections. We are a residential home inspection company in Arizona.

Target Market(s)

Real Estate

Font styles to use
Sans Serif

Requirements
Must have
• Glen Mirewick
• Home Inspector
• Velmora Property Inspections, LLC
• 480-555-0172
• glen@velmora-llc.example

```html
<!DOCTYPE html>
<html lang="en">
<head>
<meta charset="utf-8">
<title>Velmora Biz Card 2019</title>
<link rel="stylesheet" href="https://fonts.googleapis.com/css2?family=Open+Sans:wght@400;600;700;800&family=Ubuntu:wght@700&display=swap">
<style>
  :root {
    --stage-light: #f7f7f7;
    --stage-dark: #d6d6d6;
    --card-dark: #1c1c1c;
    --card-mid: #3a3a3a;
    --brand-green: #3cb54a;
    --photo-gray: #6b6e74;
    --text-light: #e6e6e6;
    --text-soft: #d4d4d4;
  }
  * { margin: 0; padding: 0; box-sizing: border-box; }
  html, body { width: 1200px; height: 1200px; overflow: hidden; }
  body {
    background: radial-gradient(ellipse at center, var(--stage-light) 0%, var(--stage-dark) 100%);
    font-family: "Open Sans", sans-serif;
    position: relative;
  }
  .card {
    position: absolute;
    width: 840px;
    height: 480px;
    overflow: hidden;
    background: linear-gradient(125deg, var(--card-mid) 0%, #2a2a2a 45%, var(--card-dark) 100%);
    box-shadow: 0 6px 14px rgba(0,0,0,0.35);
  }
  .card-front { left: 182px; top: 72px; }
  .card-back { left: 180px; top: 624px; }

  .photo-frame { position: absolute; inset: 0; }

  .wordmark {
    position: absolute;
    display: flex;
    align-items: center;
    color: var(--text-light);
    font-family: "Open Sans", sans-serif;
    font-weight: 800;
    letter-spacing: 0.02em;
    line-height: 1;
  }
  .wordmark-dot {
    background: var(--brand-green);
    border-radius: 50%;
    flex: none;
  }
  .card-front .wordmark { left: 32px; top: 156px; font-size: 40px; gap: 14px; }
  .card-front .wordmark-dot { width: 30px; height: 30px; }

  .name-line {
    position: absolute;
    left: 32px;
    top: 224px;
    white-space: nowrap;
  }
  .name-line .person-name {
    font-family: "Ubuntu", sans-serif;
    font-weight: 700;
    font-size: 26px;
    color: var(--brand-green);
    letter-spacing: 0.02em;
  }
  .name-line .person-title {
    font-family: "Open Sans", sans-serif;
    font-size: 19px;
    color: var(--text-soft);
    margin-left: 6px;
  }

  .address {
    position: absolute;
    left: 32px;
    top: 284px;
    font-size: 19px;
    line-height: 29px;
    color: var(--text-soft);
    white-space: nowrap;
  }

  .contact-list {
    position: absolute;
    left: 32px;
    top: 364px;
    list-style: none;
  }
  .contact-list li {
    display: flex;
    align-items: center;
    gap: 10px;
    height: 34px;
    font-size: 19px;
    color: var(--text-soft);
    white-space: nowrap;
  }
  .contact-list svg { width: 22px; height: 22px; flex: none; }

  .card-back .wordmark {
    left: 0; right: 0; top: 300px;
    justify-content: center;
    font-size: 72px;
    gap: 20px;
  }
  .card-back .wordmark-dot { width: 48px; height: 48px; }
  .back-url {
    position: absolute;
    left: 0; right: 0; top: 412px;
    text-align: center;
    font-size: 23px;
    letter-spacing: 0.14em;
    color: #ffffff;
  }
  .back-url strong { font-weight: 700; }
</style>
</head>
<body>

<section class="card card-front">
  <svg class="photo-frame" viewBox="0 0 840 480" width="840" height="480">
    <polygon points="354,480 665,2 840,112 840,184 668,22 370,480" fill="var(--brand-green)"/>
    <polygon points="370,480 668,22 837,172 840,184 840,480" fill="var(--photo-gray)" role="img" aria-label="Portrait photo of the home inspector in a navy company polo shirt"/>
  </svg>

  <div class="wordmark"><span class="wordmark-dot"></span>VELMORA</div>

  <p class="name-line"><span class="person-name">GLEN MIREWICK,</span><span class="person-title">HOME INSPECTOR</span></p>

  <p class="address">Velmora Property Inspections, LLC<br>Street Name, City Name, AZ</p>

  <ul class="contact-list">
    <li>
      <svg viewBox="0 0 24 24" aria-hidden="true"><circle cx="12" cy="12" r="10.5" fill="none" stroke="var(--brand-green)" stroke-width="1.6"/><path d="M9 6.5c-1.5 1-2 3-.8 5.6 1.3 2.8 3.4 4.9 5.6 5.7 1.2.4 2.2 0 2.8-.8l-2-2-1.3.8c-1.5-.8-2.6-2-3.3-3.6l1-1.1-2-4.6z" fill="var(--brand-green)"/></svg>
      480-555-0172
    </li>
    <li>
      <svg viewBox="0 0 24 24" aria-hidden="true"><path d="M2 10l10-7 10 7v11H2z" fill="var(--brand-green)"/><path d="M2 10l10 6 10-6" fill="none" stroke="#1f1f1f" stroke-width="1.4"/><rect x="8" y="8" width="8" height="1.5" fill="#1f1f1f"/></svg>
      glen@velmora-llc.example
    </li>
    <li>
      <svg viewBox="0 0 24 24" aria-hidden="true" fill="none" stroke="var(--brand-green)" stroke-width="1.5"><circle cx="12" cy="12" r="10"/><ellipse cx="12" cy="12" rx="4.5" ry="10"/><path d="M2 12h20M4 7h16M4 17h16"/></svg>
      www.velmora-llc.example
    </li>
  </ul>
</section>

<section class="card card-back">
  <div class="wordmark"><span class="wordmark-dot"></span>VELMORA</div>
  <p class="back-url">www.<strong>velmora-llc</strong>.example</p>
</section>

</body>
</html>
```